Quimby's Yard & Garden Center Business Card Update

I need an updated Business card design for my Lawn and Garden Center. We do Landscaping installs, Lawn Mowing, Snow Removal and also have a Garden Center Retail Division. I uploaded a few of our previous business cards to give an idea of what we are starting with. The main goal of this update is to simplify and modernize the business card, not all of the services that are on the previous cards has to be on the new one but I would still like to highlight our main services. There is also a sample of our logo that Can be used in the design.

Industry/Entity Type

Landscaping

Contact Information for Business Card

Morris Quimby
Morris@Quimbysyardandgarden.example
Business (555) 201-7784
Cell (555) 318-6092

Colors

Designer to choose colors to be used in the design.

Requirements
Must have
• Services Provided :
• Landscaping
• Lawn Maintenance
• Snow Removal
• Garden Center

```html
<!DOCTYPE html>
<html lang="en">
<head>
<meta charset="utf-8">
<title>Quimby's Yard &amp; Garden Center — Business Card</title>
<link rel="stylesheet" href="https://fonts.googleapis.com/css2?family=Crimson+Text:ital,wght@0,400;0,600;0,700;1,400;1,600&display=swap">
<style>
  :root {
    --backdrop: #f0f1f3;
    --card: #ffffff;
    --forest: #245028;
    --ink: #141414;
    --grass: #d9e4a6;
    --card-shadow: rgba(90, 90, 100, 0.35);
  }
  * { box-sizing: border-box; margin: 0; padding: 0; }
  html, body {
    width: 1200px;
    height: 1000px;
    overflow: hidden;
    background: var(--backdrop);
    font-family: "Crimson Text", Georgia, serif;
  }
  .stage { position: relative; width: 1200px; height: 1000px; }

  .card {
    position: absolute;
    width: 342px;
    height: 616px;
    background: var(--card);
    box-shadow: 3px 3px 6px var(--card-shadow);
    overflow: hidden;
  }
  .card--front { left: 246px; top: 123px; }
  .card--back  { left: 611px; top: 236px; }

  /* Front */
  .brand {
    position: absolute;
    left: 0; right: 0; top: 268px;
    display: flex; align-items: center; justify-content: center; gap: 12px;
    color: var(--forest);
    font-weight: 600;
    font-size: 46px;
    line-height: 1;
  }
  .brand__dot {
    width: 22px; height: 22px;
    border-radius: 50%;
    background: var(--forest);
  }

  /* Back */
  .section-title {
    position: absolute;
    right: 27px; top: 52px;
    color: var(--forest);
    font-weight: 700;
    font-size: 21px;
    letter-spacing: 0.3px;
  }
  .rule {
    position: absolute;
    left: 0; width: 316px; height: 5px;
    background: var(--forest);
  }
  .rule--top { top: 79px; }
  .rule--name { top: 325px; }

  .services {
    position: absolute;
    left: 86px; top: 124px;
    color: var(--ink);
  }
  .services__heading {
    font-size: 22px;
    font-weight: 600;
    line-height: 26px;
    margin-bottom: 1px;
  }
  .services__list { list-style: none; }
  .services__item {
    position: relative;
    font-size: 18.5px;
    line-height: 26px;
  }
  .services__item svg {
    position: absolute;
    left: -16px; top: 2px;
    width: 13px; height: 18px;
  }

  .person {
    position: absolute;
    right: 29px; top: 295px;
    color: var(--forest);
    font-style: italic;
    font-size: 22px;
  }

  .contact {
    position: absolute;
    left: 10px; top: 370px;
    list-style: none;
    color: var(--ink);
  }
  .contact__item {
    display: flex; align-items: center;
    height: 26px;
    font-size: 18px;
  }
  .contact__item svg { width: 16px; height: 16px; margin-right: 6px; flex: none; }
  .contact__item--phone { letter-spacing: 1.2px; font-size: 19px; }

  .grass {
    position: absolute;
    left: 0; right: 0; bottom: 0;
    height: 160px;
    background: linear-gradient(to bottom, rgba(217,228,166,0) 0%, var(--grass) 45%, var(--grass) 100%);
  }
</style>
</head>
<body>
<div class="stage">

  <section class="card card--front" aria-label="Business card front">
    <div class="brand">
      <span class="brand__dot"></span>
      <span class="brand__name">Quimby's</span>
    </div>
  </section>

  <section class="card card--back" aria-label="Business card back">
    <h2 class="section-title">GREENHOUSE</h2>
    <div class="rule rule--top"></div>

    <div class="services">
      <h3 class="services__heading">Services Provided :</h3>
      <ul class="services__list">
        <li class="services__item"><svg viewBox="0 0 13 18"><path d="M1 1 C10 3 13 10 11 16 C5 15 1 9 1 1 Z" fill="var(--grass)"/></svg>Landscaping</li>
        <li class="services__item"><svg viewBox="0 0 13 18"><path d="M1 1 C10 3 13 10 11 16 C5 15 1 9 1 1 Z" fill="var(--grass)"/></svg>Lawn Maintenance</li>
        <li class="services__item"><svg viewBox="0 0 13 18"><path d="M1 1 C10 3 13 10 11 16 C5 15 1 9 1 1 Z" fill="var(--grass)"/></svg>Snow Removal</li>
        <li class="services__item"><svg viewBox="0 0 13 18"><path d="M1 1 C10 3 13 10 11 16 C5 15 1 9 1 1 Z" fill="var(--grass)"/></svg>Garden Center</li>
      </ul>
    </div>

    <p class="person">Morris Quimby</p>
    <div class="rule rule--name"></div>

    <ul class="contact">
      <li class="contact__item">
        <svg viewBox="0 0 16 16"><rect x="1" y="3.5" width="14" height="9" fill="none" stroke="var(--grass)" stroke-width="1.2"/><path d="M1 3.5 L8 9 L15 3.5 M1 12.5 L6 8 M15 12.5 L10 8" fill="none" stroke="var(--grass)" stroke-width="1.2"/></svg>
        Morris@Quimbysyardandgarden.example
      </li>
      <li class="contact__item contact__item--phone">
        <svg viewBox="0 0 16 16"><path d="M3 2 L6 2 L7 5.5 L5.3 6.8 C6.2 8.8 7.4 10 9.3 10.9 L10.6 9.2 L14 10.2 L14 13.2 C8 14 2 8 3 2 Z" fill="var(--grass)"/></svg>
        (555) 201-7784
      </li>
      <li class="contact__item contact__item--phone">
        <svg viewBox="0 0 16 16"><circle cx="8" cy="8" r="6.5" fill="none" stroke="var(--grass)" stroke-width="1.4"/></svg>
        (555) 318-6092
      </li>
    </ul>

    <div class="grass" role="img" aria-label="Light green grass blades silhouette along the bottom edge"></div>
  </section>

</div>
</body>
</html>
```